High end Electrical/home automation Business Card

Need a card for a high end electrical and home automation company utilising the existing logo.
Phone
Email
Website

Like black look with raised detail. Don’t necessarily need to keep colour of logo it could be made grayscale or white etc

Target Market(s)

High end clients

Contact Information for Business Card

Ridgeline Electrical

Requirements
Must have
• Logo, phone, email, website, address

High end look
Nice to have
• Black background card
Raised font
Should not have
• Lots of colour

```html
<!DOCTYPE html>
<html lang="en">
<head>
<meta charset="utf-8">
<title>Ridgeline Electrical – Business Card</title>
<link rel="stylesheet" href="https://fonts.googleapis.com/css2?family=Arimo:wght@400;700&display=swap">
<style>
  :root {
    --stage: #c4c4c4;
    --card: #212121;
    --accent: #2394d4;
    --ink: #ffffff;
    --ink-soft: #e6e6e6;
  }
  * { margin: 0; padding: 0; box-sizing: border-box; }
  html, body { width: 1200px; height: 801px; overflow: hidden; }
  body {
    background: var(--stage);
    font-family: "Arimo", Arial, sans-serif;
    display: flex;
    align-items: center;
    justify-content: center;
    gap: 40px;
  }
  .card {
    position: relative;
    width: 540px;
    height: 309px;
    background: var(--card);
    border-radius: 18px;
    overflow: hidden;
    color: var(--ink);
  }
  .card-band { position: absolute; inset: 0; }
  .wordmark {
    position: absolute;
    display: flex;
    align-items: center;
    gap: 8px;
    font-weight: 700;
    color: var(--ink);
    white-space: nowrap;
  }
  .wordmark-dot { border-radius: 50%; background: var(--accent); flex: none; }
  .card-front .wordmark { left: 26px; top: 128px; font-size: 19px; }
  .card-front .wordmark-dot { width: 14px; height: 14px; }
  .divider {
    position: absolute;
    left: 238px; top: 58px;
    width: 1px; height: 150px;
    background: var(--accent);
  }
  .contact { position: absolute; left: 256px; top: 52px; }
  .contact-name { font-size: 21px; font-weight: 700; color: var(--accent); line-height: 1.05; }
  .contact-title { font-size: 12px; color: var(--ink-soft); margin-bottom: 10px; }
  .contact-address { font-size: 12px; color: var(--ink-soft); line-height: 1.3; margin-bottom: 8px; }
  .contact-list { list-style: none; font-size: 12px; color: var(--ink-soft); line-height: 1.5; }
  .contact-list li { display: flex; align-items: center; gap: 7px; }
  .contact-list svg { width: 11px; height: 11px; flex: none; }
  .web-domain { color: var(--accent); }
  .card-back .wordmark {
    left: 50%; top: 50%;
    transform: translate(-50%, -50%);
    font-size: 38px;
    gap: 14px;
  }
  .card-back .wordmark-dot { width: 26px; height: 26px; }
</style>
</head>
<body>

<section class="card card-front" aria-label="Business card front">
  <svg class="card-band" viewBox="0 0 540 309" aria-hidden="true">
    <path d="M150,276 C300,248 440,200 540,128 L540,140 C440,212 300,258 150,280 Z" fill="#ffffff"/>
    <path d="M0,309 L0,264 C160,258 360,220 540,146 L540,309 Z" fill="var(--accent)"/>
  </svg>

  <div class="wordmark">
    <span class="wordmark-dot"></span>
    <span>Ridgeline Electrical</span>
  </div>

  <div class="divider"></div>

  <div class="contact">
    <p class="contact-name">Dana Whitfield</p>
    <p class="contact-title">Co-Founder</p>
    <p class="contact-address">1234 Harbor Creek Rd<br>Suite C Lakeview.</p>
    <ul class="contact-list">
      <li>
        <svg viewBox="0 0 12 12"><path d="M2.5 1h2l1 3-1.3 1a6 6 0 0 0 2.8 2.8L8 6.5l3 1v2A1.5 1.5 0 0 1 9.5 11 8.5 8.5 0 0 1 1 2.5 1.5 1.5 0 0 1 2.5 1z" fill="var(--accent)"/></svg>
        555-240-7712
      </li>
      <li>
        <svg viewBox="0 0 12 12"><rect x="0.5" y="2" width="11" height="8" rx="1" fill="var(--accent)"/><path d="M1 2.6 6 6.6l5-4" fill="none" stroke="#ffffff" stroke-width="1"/></svg>
        dana@ridgelineelectrical.com
      </li>
      <li>
        <svg viewBox="0 0 12 12"><circle cx="6" cy="6" r="5.3" fill="var(--accent)"/><path d="M0.7 6h10.6M6 0.7c-2.2 2.8-2.2 7.8 0 10.6M6 0.7c2.2 2.8 2.2 7.8 0 10.6" fill="none" stroke="#ffffff" stroke-width="0.8"/></svg>
        <span>www.<span class="web-domain">ridgelineelectrical</span>.com</span>
      </li>
    </ul>
  </div>
</section>

<section class="card card-back" aria-label="Business card back">
  <div class="wordmark">
    <span class="wordmark-dot"></span>
    <span>Ridgeline Electrical</span>
  </div>
</section>

</body>
</html>
```